Eastgate AR Outfitters

Firearms Website

Requirements
Must have
• we are looking for two or three pages for a new company we are starting. The Name is Eastgate Arkansas Outfitters. The site will be EastgateArOutfitters.example (nothing on site at this time) We will be selling mainly handguns and products for self defense. We want this site to focus on the handgun and ammo sells as well as low cost transfers. we will handle the ecommerce part) We want a

1.) main page, mainly general information on the company.

2.) a page for sells. we will be adding the guns by hand as we place them for sell and use our credit card process. We just need the layout to fill in the items for sale on this page.

3.) navigation will be.. HOME - SALES (((guns and gun Accessories)) and self defense products) - Contact US- Transfers

company info

Eastgate Arkansas Outfitters

EastgateAROutfitters.example

sales@EastgateAROutfitters.example

855-Tool 2 Shop (855-555-0142) same number for fax

412 west Harlan avenue

Kosciusko, ms. 71234

```html
<!DOCTYPE html>
<html lang="en">
<head>
<meta charset="utf-8">
<title>Eastgate Arkansas Outfitters</title>
<link href="https://fonts.googleapis.com/css2?family=Didact+Gothic&display=swap" rel="stylesheet">
<style>
:root{
  --orange:#f26b1d;
  --orange-light:#f7932f;
  --gold:#d9a21a;
  --black:#000;
  --ink:#222;
  --muted-head:#4a4a4a;
  --muted-text:#3a3a3a;
  --white:#fff;
}
*{box-sizing:border-box;margin:0;padding:0}
html,body{width:971px;height:1200px;overflow:hidden;background:var(--white)}
body{font-family:"Didact Gothic",sans-serif;color:var(--ink);position:relative}
.abs{position:absolute}

/* top navigation */
.topbar{left:0;top:0;width:971px;height:57px;background:linear-gradient(#fdfdfd,#e9e9e9);border-bottom:2px solid #cfcfcf}
.logo-slot{left:38px;top:17px;font-size:13px;color:#555}
.main-nav{left:178px;top:0;display:flex;height:57px}
.main-nav a{width:135px;height:57px;border-left:1px solid #ddd;display:flex;justify-content:center;padding-top:17px;font-size:13px;color:#666;text-decoration:none}
.main-nav a:last-child{border-right:1px solid #ddd}

/* hero */
.hero{left:0;top:59px;width:971px;height:450px;
  background:
    radial-gradient(ellipse 120px 160px at 350px 280px,rgba(232,178,30,.55),rgba(232,178,30,0) 70%),
    radial-gradient(ellipse 340px 170px at 640px 160px,#5c5c5c 0%,#363636 45%,rgba(30,30,30,0) 100%),
    radial-gradient(ellipse 200px 90px at 520px 400px,#3e3a36,rgba(20,20,20,0) 100%),
    linear-gradient(160deg,#111 0%,#1f1f1f 40%,#2b2b2b 60%,#0d0d0d 100%);
  border-bottom:2px solid #cfcfcf}
.dropdown{left:179px;top:59px;width:135px;height:154px;background:rgba(0,0,0,.78);border-top:2px solid var(--orange)}
.dropdown a{display:block;height:36px;line-height:36px;padding-left:37px;font-size:13px;color:#eee;text-decoration:none}
.dropdown a.active{background:linear-gradient(var(--orange-light),var(--orange))}
.search{left:795px;top:94px;width:176px;height:29px;background:linear-gradient(90deg,var(--orange),var(--orange-light));color:#fff;font-size:14px;padding:5px 0 0 16px}
.search svg{position:absolute;right:10px;top:8px}
.brand-band{left:0;top:277px;width:360px;height:190px;background:rgba(0,0,0,.5);border-top:1px solid #6b4a2a}
.brand-name{left:13px;top:321px;font-size:25px;line-height:31px;color:var(--white);text-transform:uppercase;letter-spacing:.5px}
.brand-phone{left:19px;top:439px;font-size:13px;color:#fff}
.caption{left:608px;top:316px;width:363px;height:158px;background:rgba(0,0,0,.5)}
.caption p{position:absolute;right:16px;top:18px;width:330px;text-align:right;font-size:11px;line-height:19px;color:#fff}
.btn{display:inline-block;height:29px;padding:0 8px;line-height:28px;border-radius:5px;border:1px solid #fbb07a;background:linear-gradient(var(--orange-light),var(--orange));color:#fff;font-size:15px}
.btn b{font-weight:700}
.caption .btn{position:absolute;left:54px;top:102px}
.dots{left:857px;top:446px;display:flex;gap:8px}
.dots span{width:11px;height:11px;border-radius:50%;background:var(--orange)}
.dots span.on{background:none;border:2px solid var(--orange)}

/* store */
.strip{left:0;top:511px;width:971px;height:34px;background:linear-gradient(#e6e6e6,#fff)}
.store{left:0;top:545px;width:971px;height:160px;background:linear-gradient(#fafafa,#f0f0f0)}
.store-title{left:0;top:557px;width:971px;text-align:center;font-size:15px;color:#333}
.rule{left:108px;top:583px;width:742px;height:1px;background:#ddd}
.dark{left:0;top:705px;width:971px;height:357px;background:var(--black);border-top:4px solid #d6d6d6}
.card{top:607px;width:253px;height:161px;background:#fff;padding:5px;box-shadow:0 1px 3px rgba(0,0,0,.3)}
.card .photo{width:100%;height:100%;position:relative}
.photo-pistol{background:
  radial-gradient(ellipse 90px 40px at 120px 80px,#c9c9c9,rgba(150,150,150,0) 100%),
  radial-gradient(ellipse 70px 50px at 150px 60px,#1a1a1a,rgba(26,26,26,0) 100%),
  linear-gradient(160deg,#8a8a8a 0%,#4c4c4c 45%,#1e1e1e 100%)}
.photo-chrome{background:
  radial-gradient(ellipse 110px 45px at 130px 70px,#e8e8e8,rgba(200,200,200,0) 100%),
  radial-gradient(ellipse 80px 40px at 70px 110px,#161616,rgba(20,20,20,0) 100%),
  linear-gradient(170deg,#9a9a9a 0%,#555 50%,#2a2a2a 100%)}
.photo-revolver{background:
  radial-gradient(ellipse 30px 16px at 190px 85px,rgba(201,150,40,.7),rgba(201,150,40,0) 100%),
  radial-gradient(ellipse 110px 40px at 110px 70px,#8e8e8e,rgba(140,140,140,0) 100%),
  linear-gradient(160deg,#f7f7f7 0%,#e4e4e4 60%,#d2d2d2 100%)}
.price{position:absolute;right:0;bottom:16px;width:175px;height:30px;background:rgba(70,70,70,.55);color:#fff;font-size:12px;text-align:right;padding:8px 10px 0 0}
.price.plain{background:none;color:#333;bottom:14px}
.arrow{top:672px}
.stars{top:773px;display:flex;gap:10px}
.brands{top:806px;width:971px;height:77px;border-top:1px solid #222;border-bottom:1px solid #222}
.brand-col{width:300px;text-align:center}
.brand-col h3{font-weight:400;font-size:19px;color:var(--muted-head)}
.brand-col p{font-size:13px;margin-top:9px;color:var(--muted-text)}
.brand-col.current h3,.brand-col.current p{color:#fff}
.person{left:60px;top:903px;width:218px;height:146px;border:1px solid var(--orange);
  background:
    radial-gradient(ellipse 38px 48px at 85px 52px,#1c1c1c,rgba(28,28,28,0) 100%),
    radial-gradient(ellipse 75px 60px at 120px 130px,#222,rgba(34,34,34,0) 100%),
    radial-gradient(ellipse 30px 20px at 70px 100px,rgba(210,160,130,.6),rgba(210,160,130,0) 100%),
    #fff}
.play{left:148px;top:948px}
.about{left:311px;top:914px;width:600px;font-size:11px;line-height:19px;color:#fff}
.about-small{left:312px;top:1011px;font-size:8.5px;color:#fff}
.about-btn{left:607px;top:1004px}
.social{left:776px;top:1048px;width:170px;height:34px;background:var(--orange);display:flex;justify-content:space-around;align-items:center;padding:0 12px}
.social span{width:20px;height:20px;border-radius:50%;border:1.5px solid #fff}

/* footer */
.foot-nav{left:0;top:1062px;width:971px;height:55px;display:flex;justify-content:center;padding-top:19px}
.foot-nav a{font-size:13px;color:#555;text-decoration:none;margin:0 26px}
.contact{left:0;top:1117px;width:971px;height:59px;background:linear-gradient(#ececec,#f7f7f7);font-size:11px;color:#777}
.contact .item{position:absolute;top:21px;display:flex;align-items:center;gap:10px}
.copyright{left:0;top:1176px;width:971px;height:24px;background:var(--orange);color:#fff;font-size:11px;text-align:center;line-height:24px}
</style>
</head>
<body>

<header class="abs topbar"></header>
<div class="abs logo-slot">Your logo here</div>
<nav class="abs main-nav">
  <a href="#">Home</a><a href="#">Sales</a><a href="#">Self Defense</a><a href="#">Contact us</a><a href="#">Transfers</a>
</nav>

<section class="abs hero" role="img" aria-label="Dark close-up photograph of a semi-automatic handgun with cartridges and a gold wing emblem"></section>
<div class="abs brand-band"></div>
<div class="abs brand-name">Eastgate Arkansas<br>Outfitters</div>
<div class="abs brand-phone">855-Tool 2 Shop</div>

<nav class="abs dropdown">
  <a href="#">Browse</a><a href="#" class="active">Featured</a><a href="#">Cool stuff</a><a href="#">New Version</a>
</nav>
<div class="abs search">Search
  <svg width="14" height="14" viewBox="0 0 14 14"><circle cx="5.5" cy="5.5" r="4" fill="none" stroke="#fff" stroke-width="2"/><line x1="8.5" y1="8.5" x2="13" y2="13" stroke="#fff" stroke-width="2"/></svg>
</div>

<div class="abs caption">
  <p>Lorem Ipsum dolor sit amet, consectetuer adipiscingelit. Duis tellus. Donec ante dolor, iaculis nec, gravidaac, cursus in, eros. Mauris vestibulum, felis et egestasullamcorper, purus nibh vehicula sem, eu egestas antenisl non justo.</p>
  <span class="btn"><b>Shop</b> now</span>
</div>
<div class="abs dots"><span></span><span class="on"></span><span></span><span></span><span></span></div>

<div class="abs strip"></div>
<section class="abs store"></section>
<div class="abs store-title">Check our online store</div>
<div class="abs rule"></div>
<section class="abs dark"></section>

<svg class="abs arrow" style="left:40px" width="10" height="16" viewBox="0 0 10 16"><polygon points="10,0 0,8 10,16" fill="#f26b1d"/></svg>
<svg class="abs arrow" style="left:922px" width="10" height="16" viewBox="0 0 10 16"><polygon points="0,0 10,8 0,16" fill="#f26b1d"/></svg>

<article class="abs card" style="left:78px"><div class="photo photo-pistol" role="img" aria-label="Black and white photo of a compact pistol"><div class="price">$234.00</div></div></article>
<article class="abs card" style="left:355px"><div class="photo photo-chrome" role="img" aria-label="Black and white photo of a large chrome pistol"><div class="price">$234.00</div></div></article>
<article class="abs card" style="left:634px"><div class="photo photo-revolver" role="img" aria-label="Photo of a scoped revolver with cartridges"><div class="price plain">$234.00</div></div></article>

<div class="abs stars" style="left:148px">
  <svg width="14" height="13" viewBox="0 0 14 13"><polygon points="7,0 8.7,4.6 13.5,4.7 9.7,7.7 11.1,12.5 7,9.7 2.9,12.5 4.3,7.7 0.5,4.7 5.3,4.6" fill="#f7932f"/></svg>
  <svg width="14" height="13" viewBox="0 0 14 13"><polygon points="7,0 8.7,4.6 13.5,4.7 9.7,7.7 11.1,12.5 7,9.7 2.9,12.5 4.3,7.7 0.5,4.7 5.3,4.6" fill="#f7932f"/></svg>
  <svg width="14" height="13" viewBox="0 0 14 13"><polygon points="7,0 8.7,4.6 13.5,4.7 9.7,7.7 11.1,12.5 7,9.7 2.9,12.5 4.3,7.7 0.5,4.7 5.3,4.6" fill="#f7932f"/></svg>
  <svg width="14" height="13" viewBox="0 0 14 13"><polygon points="7,0 8.7,4.6 13.5,4.7 9.7,7.7 11.1,12.5 7,9.7 2.9,12.5 4.3,7.7 0.5,4.7 5.3,4.6" fill="#f7932f"/></svg>
  <svg width="14" height="13" viewBox="0 0 14 13"><polygon points="7,0 8.7,4.6 13.5,4.7 9.7,7.7 11.1,12.5 7,9.7 2.9,12.5 4.3,7.7 0.5,4.7 5.3,4.6" fill="#fff"/></svg>
</div>
<div class="abs stars" style="left:425px">
  <svg width="14" height="13" viewBox="0 0 14 13"><polygon points="7,0 8.7,4.6 13.5,4.7 9.7,7.7 11.1,12.5 7,9.7 2.9,12.5 4.3,7.7 0.5,4.7 5.3,4.6" fill="#f7932f"/></svg>
  <svg width="14" height="13" viewBox="0 0 14 13"><polygon points="7,0 8.7,4.6 13.5,4.7 9.7,7.7 11.1,12.5 7,9.7 2.9,12.5 4.3,7.7 0.5,4.7 5.3,4.6" fill="#f7932f"/></svg>
  <svg width="14" height="13" viewBox="0 0 14 13"><polygon points="7,0 8.7,4.6 13.5,4.7 9.7,7.7 11.1,12.5 7,9.7 2.9,12.5 4.3,7.7 0.5,4.7 5.3,4.6" fill="#f7932f"/></svg>
  <svg width="14" height="13" viewBox="0 0 14 13"><polygon points="7,0 8.7,4.6 13.5,4.7 9.7,7.7 11.1,12.5 7,9.7 2.9,12.5 4.3,7.7 0.5,4.7 5.3,4.6" fill="#f7932f"/></svg>
  <svg width="14" height="13" viewBox="0 0 14 13"><polygon points="7,0 8.7,4.6 13.5,4.7 9.7,7.7 11.1,12.5 7,9.7 2.9,12.5 4.3,7.7 0.5,4.7 5.3,4.6" fill="#f7932f"/></svg>
</div>
<div class="abs stars" style="left:706px">
  <svg width="14" height="13" viewBox="0 0 14 13"><polygon points="7,0 8.7,4.6 13.5,4.7 9.7,7.7 11.1,12.5 7,9.7 2.9,12.5 4.3,7.7 0.5,4.7 5.3,4.6" fill="#f7932f"/></svg>
  <svg width="14" height="13" viewBox="0 0 14 13"><polygon points="7,0 8.7,4.6 13.5,4.7 9.7,7.7 11.1,12.5 7,9.7 2.9,12.5 4.3,7.7 0.5,4.7 5.3,4.6" fill="#f7932f"/></svg>
  <svg width="14" height="13" viewBox="0 0 14 13"><polygon points="7,0 8.7,4.6 13.5,4.7 9.7,7.7 11.1,12.5 7,9.7 2.9,12.5 4.3,7.7 0.5,4.7 5.3,4.6" fill="#f7932f"/></svg>
  <svg width="14" height="13" viewBox="0 0 14 13"><polygon points="7,0 8.7,4.6 13.5,4.7 9.7,7.7 11.1,12.5 7,9.7 2.9,12.5 4.3,7.7 0.5,4.7 5.3,4.6" fill="#f7932f"/></svg>
  <svg width="14" height="13" viewBox="0 0 14 13"><polygon points="7,0 8.7,4.6 13.5,4.7 9.7,7.7 11.1,12.5 7,9.7 2.9,12.5 4.3,7.7 0.5,4.7 5.3,4.6" fill="#fff"/></svg>
</div>

<div class="abs brands"></div>
<div class="abs brand-col" style="left:5px;top:810px"><h3>Popular brands</h3><p>Check all the popular stuff in this section</p></div>
<div class="abs brand-col current" style="left:332px;top:810px"><h3>New brands</h3><p>Check all the new stuff in this section</p></div>
<div class="abs brand-col" style="left:646px;top:810px"><h3>Featured brands</h3><p>Check all the feature stuff in this section</p></div>
<svg class="abs" style="left:308px;top:835px" width="10" height="16" viewBox="0 0 10 16"><polygon points="10,0 0,8 10,16" fill="#f26b1d"/></svg>
<svg class="abs" style="left:645px;top:835px" width="10" height="16" viewBox="0 0 10 16"><polygon points="0,0 10,8 0,16" fill="#f26b1d"/></svg>

<div class="abs person" role="img" aria-label="Video still of a hooded man in dark clothing aiming a pistol, white background"></div>
<svg class="abs play" width="40" height="40" viewBox="0 0 40 40"><circle cx="20" cy="20" r="18" fill="none" stroke="rgba(255,255,255,.85)" stroke-width="2"/><polygon points="15,11 29,20 15,29" fill="none" stroke="rgba(255,255,255,.85)" stroke-width="2"/></svg>
<p class="abs about">Lorem Ipsum dolor sit amet, consectetuer adipiscingelit. Duis tellus. Donec ante dolor, iaculis nec, gravidaac, cursus in, eros. Mauris vestibulum, felis et egestasullamcorper, purus nibh vehicula sem, eu egestas antenisl non justo. Fusce tincidunt, lorem nec dapibusconsectetuer, leo orci mollis ipsum, eget suscipit erospurus in ante.</p>
<p class="abs about-small">Lorem Ipsum dolor sit amet,consectetur adipisicing elit, sed do.</p>
<span class="abs btn about-btn"><b>Shop</b> now</span>

<div class="abs social" aria-label="Social links"><span></span><span></span><span></span><span></span></div>

<nav class="abs foot-nav">
  <a href="#">Home</a><a href="#">Sales</a><a href="#">Self Defense</a><a href="#">Contact us</a><a href="#">Transfers</a>
</nav>

<footer class="abs contact">
  <div class="item" style="left:175px">
    <svg width="18" height="17" viewBox="0 0 18 17"><polygon points="9,0 18,8 15,8 15,17 11,17 11,11 7,11 7,17 3,17 3,8 0,8" fill="#888"/></svg>
    <span>412 west Harlan avenue Kosciusko, ms. 71234</span>
  </div>
  <div class="item" style="left:455px">
    <svg width="16" height="20" viewBox="0 0 16 20"><path d="M12 1 C8 5 4 12 3 19" stroke="#888" stroke-width="3" fill="none" stroke-linecap="round"/></svg>
    <span>855-555-0142</span>
  </div>
  <div class="item" style="left:588px">
    <svg width="20" height="14" viewBox="0 0 20 14"><rect x="0" y="2" width="20" height="12" fill="#888"/><polyline points="0,2 10,8 20,2" fill="none" stroke="#eee" stroke-width="1.5"/></svg>
    <span>sales@EastgateAROutfitters.example</span>
  </div>
</footer>
<div class="abs copyright">Eastgate Arkansas Outfitters &nbsp; © 2013 | Privacy Policy</div>

</body>
</html>
```